Innovative Event Ticketing Start Up. Needs a Web Design

We need a web design for a new company based in London called 'Brimwell'. We are a platform which facilitates the building of groups of customers for events. As more people commit to an event, the price incrementally decreases. We would like there to be an emphasis on the sharing element and the decreasing price with higher participation.

Any quieres please email me at jrvk58@postvale.com

Target Market(s)

18-30 year olds who are active and savvy across social media sites

Industry/Entity Type

Events

Number of Pages Required

3 page

Font styles to use
Other font styles liked:
• Phi Roman

Requirements
Must have
• Each event offering runs for a limited time so a countdown timer is also to be included as well as a counter of number of participants (please find example attached).
• The interface needs to have the options for 'Live 'Music', 'Nightlife', 'Festivals', 'Comedy' and 'Everything Else'. Also
• A 'featured' section, for our promoted events
• Social sharing icons for Friendloom, Zephly, Pingrove, SMS and Email
• Room the inclusion of a video
• Pages for clients to sign up - registering details ect.
• Content is still being completed, so room available to add when ready
Nice to have
• An interface design we like as a guiding templates on is https://quorvexapp.com/
• Velto wordpress theme is also of interest.
• Scroll over clicking for main interface and also for the event once clicked upon.
• Event pages similar desgin to quorvex with same features such as Orvane Atlas but also participant counter and affiliate marketing options.
Should not have
• CMS no longer necessary

```html
<!DOCTYPE html>
<html lang="en">
<head>
<meta charset="utf-8">
<title>Brimwell – Events in London</title>
<link href="https://fonts.googleapis.com/css2?family=Lato:wght@400;700;900&family=Open+Sans:wght@400;600;700&display=swap" rel="stylesheet">
<style>
:root{
  --orange:#f26430;
  --orange-dark:#e0521f;
  --orange-soft:#f79a72;
  --ink:#222;
  --text:#555;
  --muted:#888;
  --line:#e4e4e4;
  --panel:#f5f5f5;
  --night:#1d1d1f;
  --white:#fff;
}
*{box-sizing:border-box;margin:0;padding:0}
html,body{width:1200px;height:3296px;overflow:hidden}
body{font-family:"Open Sans",Arial,sans-serif;color:var(--text);background:var(--white);font-size:13px;position:relative}
h1,h2,h3,h4{font-family:"Lato",Arial,sans-serif;color:var(--ink)}
a{color:inherit;text-decoration:none}

/* header */
.site-header{position:absolute;top:0;left:0;width:1200px;height:64px;background:rgba(20,20,22,.92);display:flex;align-items:center;z-index:3}
.brand{display:flex;align-items:center;gap:10px;height:64px;padding:0 22px;background:var(--orange);color:#fff;font-family:"Lato",sans-serif;font-weight:900;font-size:20px;letter-spacing:1px}
.brand-mark{width:24px;height:24px;background:#fff;border-radius:3px}
.main-nav{display:flex;margin-left:60px}
.main-nav a{color:#fff;font-size:12px;font-weight:600;padding:0 17px;line-height:64px;letter-spacing:.5px}
.main-nav a.is-active{background:var(--orange)}
.account{margin-left:auto;display:flex;height:64px;background:#333}
.account a{color:#fff;font-size:12px;font-weight:600;padding:0 16px;line-height:64px}
.account a+a{border-left:1px solid #555}

/* hero */
.hero{position:absolute;top:0;left:0;width:1200px;height:520px;background:linear-gradient(180deg,#2a1f1e 0%,#3d2a24 45%,#5b3a2c 75%,#2b211f 100%)}
.hero-photo{position:absolute;inset:0;background:radial-gradient(ellipse at 50% 70%,rgba(196,120,80,.45),transparent 60%),radial-gradient(ellipse at 15% 80%,rgba(120,80,60,.5),transparent 50%),radial-gradient(ellipse at 85% 80%,rgba(120,80,60,.5),transparent 50%)}
.hero-inner{position:absolute;top:190px;left:0;width:1200px;text-align:center}
.hero h1{color:#fff;font-size:38px;font-weight:700}
.hero p{color:#eee;font-size:13px;line-height:20px;width:600px;margin:14px auto 0}
.search{display:flex;width:580px;margin:26px auto 0;height:42px}
.search input{flex:1;border:0;padding:0 16px;font-size:12px;font-family:inherit;color:var(--muted)}
.search button{width:110px;border:0;background:var(--orange);color:#fff;font-size:15px;font-weight:600;font-family:inherit}
.hero-arrow{position:absolute;top:268px;width:20px;height:20px}
.hero-arrow.left{left:28px}.hero-arrow.right{right:28px}

/* date bar */
.date-bar{position:absolute;top:520px;left:0;width:1200px;height:44px;background:var(--orange);color:#fff;font-weight:600;font-size:14px}
.date-bar .date{position:absolute;left:378px;top:12px}
.date-bar .time{position:absolute;left:672px;top:12px}
.clock{position:absolute;left:565px;top:-26px;width:70px;height:70px;border-radius:50%;background:var(--orange);border:4px solid #fff}

/* stats */
.stats{position:absolute;top:564px;left:0;width:1200px;height:96px;background:var(--panel);border-bottom:1px solid var(--line);display:flex;justify-content:center}
.stat{width:236px;display:flex;align-items:center;gap:12px;padding-left:30px}
.stat-icon{width:38px;height:38px;border-radius:50%;border:2px solid #444;display:flex;align-items:center;justify-content:center}
.stat strong{display:block;color:var(--ink);font-size:14px;font-family:"Lato",sans-serif}
.stat span{font-size:11px;color:var(--muted)}

/* section titles */
.section-title{text-align:center;font-size:26px;font-weight:700}

/* upcoming */
.upcoming{position:absolute;top:660px;left:0;width:1200px;height:590px}
.upcoming .section-title{margin-top:108px}
.cards{display:flex;gap:48px;justify-content:center;margin-top:30px}
.event-card{width:280px;background:#fff;border:1px solid var(--line)}
.event-photo{height:104px}
.event-body{position:relative;padding:10px 12px 12px 60px;height:142px}
.date-badge{position:absolute;left:10px;top:10px;width:40px;height:46px;background:var(--orange);color:#fff;text-align:center;font-family:"Lato",sans-serif;line-height:1}
.date-badge b{display:block;font-size:20px;padding-top:6px}
.date-badge small{font-size:9px;font-weight:700}
.stars{position:absolute;left:10px;top:62px;color:var(--orange);font-size:9px;letter-spacing:-1px}
.event-body h3{color:var(--orange);font-size:13px;font-weight:700}
.meta{font-size:10px;color:var(--text);margin-top:4px;line-height:15px}
.desc{font-size:9.5px;color:var(--muted);line-height:13px;margin-top:5px}
.card-foot{display:flex;align-items:center;justify-content:space-between;margin:6px 0 0 -48px}
.card-foot a{font-size:10px;color:var(--muted)}
.share{display:flex;gap:3px}
.share i{width:14px;height:14px;background:var(--orange);display:block}
.more-btn{display:block;width:116px;margin:50px auto 0;border:1px solid #ccc;background:#f4f4f4;text-align:center;font-size:11px;line-height:28px;color:var(--text)}

/* video */
.video-band{position:absolute;top:1250px;left:0;width:1200px;height:500px;background:linear-gradient(180deg,#4d5560,#6e747c 50%,#8b8e90)}
.browser{position:absolute;top:1340px;left:144px;width:912px;height:490px;background:#fff;box-shadow:0 6px 24px rgba(0,0,0,.3);border:1px solid #ccc}
.browser-bar{height:30px;background:#e9e9e9;display:flex;align-items:center;gap:6px;padding-left:12px}
.browser-bar i{width:10px;height:10px;border-radius:50%;background:#c8c8c8;display:block}
.browser-bar .url{margin-left:14px;width:360px;height:18px;background:#fff;border:1px solid #d5d5d5;font-size:10px;line-height:16px;padding-left:8px;color:var(--muted)}
.video-frame{position:absolute;top:30px;left:0;right:0;bottom:28px;background:linear-gradient(160deg,#c7a58a 0%,#d88e6a 35%,#5fb6d3 70%,#2f8fb3 100%)}
.video-controls{position:absolute;left:0;right:0;bottom:0;height:28px;background:#111;display:flex;align-items:center;padding:0 12px;gap:12px}
.video-controls .track{flex:1;height:3px;background:#555}
.video-controls .track span{display:block;width:22%;height:3px;background:var(--orange)}
.video-caption{position:absolute;top:1840px;left:0;width:1200px;text-align:center}
.video-caption svg{display:block;margin:34px auto 10px}
.video-caption h2{font-size:22px}
.video-caption p{width:1040px;margin:20px auto 0;font-size:10.5px;line-height:15px;color:var(--muted)}

/* promoted */
.promoted{position:absolute;top:2030px;left:0;width:1200px;height:420px;display:flex}
.promo-list{width:600px;background:var(--orange-dark);padding:40px 0 0 128px;color:#fff}
.promo-list h2{color:#fff;font-size:22px;border-bottom:1px solid rgba(255,255,255,.35);padding-bottom:14px;width:420px}
.promo-list h3{color:#ffd9c6;font-size:16px;margin-top:22px}
.promo-list ul{list-style:none;margin-top:12px}
.promo-list li{font-size:11px;line-height:23px;padding-left:16px;position:relative}
.promo-list li:before{content:"";position:absolute;left:0;top:9px;width:6px;height:6px;background:#fff;border-radius:1px}
.btn-outline{display:inline-block;margin-top:18px;border:1px solid #fff;color:#fff;font-size:12px;padding:6px 16px}
.promo-create{width:600px;background:var(--orange-soft);text-align:center;padding-top:86px}
.create-icon{width:74px;height:74px;background:var(--orange);border-radius:12px;margin:0 auto;border:3px solid #fff}
.promo-create h2{color:#fff;font-size:20px;margin-top:24px}
.promo-create p{color:#fff;font-size:11px;line-height:16px;width:320px;margin:8px auto 0}
.btn-solid{display:inline-block;margin-top:14px;background:var(--orange);color:#fff;font-size:12px;padding:7px 18px;border-radius:2px}

/* categories */
.categories{position:absolute;top:2450px;left:0;width:1200px;height:600px}
.categories .section-title{margin-top:58px}
.tabs{display:flex;justify-content:center;gap:6px;margin-top:18px}
.tabs a{font-size:10px;padding:3px 12px;color:var(--muted)}
.tabs a.is-active{background:var(--orange);color:#fff;border-radius:2px}
.tile{position:absolute;display:flex;align-items:center;justify-content:center}
.tile h4{color:#fff;font-size:16px;font-weight:700}
.tile.sports{left:128px;top:150px;width:432px;height:408px;background:linear-gradient(160deg,#d44a3a,#7a2d2a 55%,#3a3a3d)}
.tile.balloons{left:580px;top:150px;width:492px;height:190px;background:linear-gradient(180deg,#87a7d8,#d88a4a 70%,#6e4a38)}
.tile.music{left:580px;top:354px;width:240px;height:204px;background:linear-gradient(160deg,#3a2c54,#7b3c6b 60%,#c56a5a)}
.tile.festivals{left:832px;top:354px;width:240px;height:204px;background:linear-gradient(160deg,#3b6fb5,#a04a8a 55%,#e08a4a)}

/* footer */
.site-footer{position:absolute;top:3050px;left:0;width:1200px;height:212px;background:var(--orange);color:#fff;display:flex;padding:42px 0 0 128px}
.foot-col{width:186px}
.foot-col h4{color:#fff;font-size:12px;margin-bottom:10px}
.foot-col li{list-style:none;font-size:10px;line-height:18px;padding-left:12px;position:relative}
.foot-col li:before{content:"›";position:absolute;left:0}
.foot-brand{margin-left:60px;margin-top:24px;height:40px;display:flex;align-items:center;gap:10px;font-family:"Lato",sans-serif;font-weight:900;font-size:28px;letter-spacing:1px}
.foot-brand span{width:38px;height:38px;background:#fff;border-radius:4px}
.copyright{position:absolute;top:3262px;left:0;width:1200px;height:34px;background:#c9461a;color:#fff;font-size:10px;text-align:center;line-height:34px}
</style>
</head>
<body>

<header class="site-header">
  <a class="brand" href="#"><span class="brand-mark"></span>BRIMWELL</a>
  <nav class="main-nav">
    <a class="is-active" href="#">HOME</a><a href="#">ABOUT US</a><a href="#">MUSIC</a><a href="#">NIGHTLIFE</a><a href="#">FESTIVALS</a><a href="#">COMEDY</a><a href="#">EVERYTHING ELSE</a>
  </nav>
  <div class="account"><a href="#">SIGN UP</a><a href="#">LOGIN</a></div>
</header>

<section class="hero">
  <div class="hero-photo" role="img" aria-label="Crowd of people at a lively London event under stage lights"></div>
  <svg class="hero-arrow left" viewBox="0 0 20 20"><path d="M13 3 6 10l7 7" fill="none" stroke="#fff" stroke-width="2"/></svg>
  <svg class="hero-arrow right" viewBox="0 0 20 20"><path d="M7 3l7 7-7 7" fill="none" stroke="#fff" stroke-width="2"/></svg>
  <div class="hero-inner">
    <h1>Meet your next awesome Fun Experience</h1>
    <p>Gather friends, commit together and watch the ticket price drop as more people join. The bigger the group, the better the deal for everyone going.</p>
    <form class="search"><input type="text" value="Search your event by name or venue"><button type="button">Search</button></form>
  </div>
</section>

<div class="date-bar">
  <span class="date">24 September 2015</span>
  <div class="clock">
    <svg width="62" height="62" viewBox="0 0 62 62"><circle cx="31" cy="31" r="17" fill="none" stroke="#fff" stroke-width="3"/><path d="M31 21v10l7 5" fill="none" stroke="#fff" stroke-width="3"/></svg>
  </div>
  <span class="time">Event Time 12:00 PM</span>
</div>

<section class="stats">
  <div class="stat"><div class="stat-icon"><svg width="18" height="18" viewBox="0 0 18 18"><path d="M9 1a6 6 0 0 0-6 6c0 5 6 10 6 10s6-5 6-10a6 6 0 0 0-6-6z" fill="#444"/><circle cx="9" cy="7" r="2" fill="#f5f5f5"/></svg></div><div><strong>London</strong><span>Southbank, SE1</span></div></div>
  <div class="stat"><div class="stat-icon"><svg width="18" height="18" viewBox="0 0 18 18"><path d="M7 3v9a3 3 0 1 1-2-2.8V1h9v3H7z" fill="#444"/></svg></div><div><strong>Live Music</strong><span>Best experiences</span></div></div>
  <div class="stat"><div class="stat-icon"><svg width="18" height="18" viewBox="0 0 18 18"><circle cx="9" cy="6" r="3.5" fill="#444"/><path d="M2 17c0-4 3-6 7-6s7 2 7 6z" fill="#444"/></svg></div><div><strong>100 Sponsor</strong><span>Great deals and prizes</span></div></div>
  <div class="stat"><div class="stat-icon"><svg width="18" height="18" viewBox="0 0 18 18"><rect x="2" y="5" width="14" height="9" rx="1" fill="#444"/><rect x="4" y="2" width="10" height="4" fill="#444"/></svg></div><div><strong>1458 Seats</strong><span>Hurry up, register!</span></div></div>
</section>

<section class="upcoming">
  <h2 class="section-title">Now Upcoming Event in London</h2>
  <div class="cards">
    <article class="event-card">
      <div class="event-photo" role="img" aria-label="Fashion runway show with models and audience" style="background:linear-gradient(160deg,#5a4a6a,#b98a8a 55%,#e0d2c8)"></div>
      <div class="event-body">
        <div class="date-badge"><b>20</b><small>SEP</small></div><div class="stars">★★★★★</div>
        <h3>London Runway Weekend</h3>
        <p class="meta">◷ Sep 2016 • 10am-5pm<br>⌖ Hollin Hall, London</p>
        <p class="desc">Join a group of friends and unlock cheaper tickets as more people sign up.</p>
        <div class="card-foot"><a href="#">Get Tickets</a><div class="share"><i></i><i></i><i></i><i></i><i></i></div></div>
      </div>
    </article>
    <article class="event-card">
      <div class="event-photo" role="img" aria-label="Crowd dancing at an outdoor night party" style="background:linear-gradient(160deg,#2b4a8a,#7a5aa8 55%,#e6a06a)"></div>
      <div class="event-body">
        <div class="date-badge"><b>22</b><small>SEP</small></div><div class="stars">★★★★★</div>
        <h3>London The Temple Tours</h3>
        <p class="meta">◷ Sep 2016 • 8pm-2am<br>⌖ Marrowgate Arches, London</p>
        <p class="desc">The more people commit to this night, the lower the price for everyone.</p>
        <div class="card-foot"><a href="#">Get Tickets</a><div class="share"><i></i><i></i><i></i><i></i><i></i></div></div>
      </div>
    </article>
    <article class="event-card">
      <div class="event-photo" role="img" aria-label="Friends celebrating on a party boat" style="background:linear-gradient(160deg,#3a8ac8,#8ac0e0 50%,#e8b48a)"></div>
      <div class="event-body">
        <div class="date-badge"><b>24</b><small>SEP</small></div><div class="stars">★★★★★</div>
        <h3>London Boat Party</h3>
        <p class="meta">◷ Sep 2016 • 6pm-11pm<br>⌖ Quaymere Dock, London</p>
        <p class="desc">Share with your crew, fill the boat and watch the ticket price fall.</p>
        <div class="card-foot"><a href="#">Get Tickets</a><div class="share"><i></i><i></i><i></i><i></i><i></i></div></div>
      </div>
    </article>
  </div>
  <a class="more-btn" href="#">Show Me More</a>
</section>

<div class="video-band" role="img" aria-label="Blurred festival crowd backdrop"></div>
<div class="browser">
  <div class="browser-bar"><i></i><i></i><i></i><span class="url">www.brimwell.com</span></div>
  <div class="video-frame" role="img" aria-label="Startup video still of friends having fun in a pool"></div>
  <div class="video-controls">
    <svg width="10" height="12" viewBox="0 0 10 12"><path d="M0 0l10 6-10 6z" fill="#fff"/></svg>
    <div class="track"><span></span></div>
    <svg width="14" height="12" viewBox="0 0 14 12"><path d="M0 4h3l4-4v12L3 8H0z" fill="#fff"/></svg>
  </div>
</div>
<section class="video-caption">
  <svg width="24" height="18" viewBox="0 0 24 18"><rect x="0" y="3" width="16" height="12" rx="2" fill="#444"/><path d="M17 7l7-4v12l-7-4z" fill="#444"/></svg>
  <h2>Brimwell Events! Startup Video</h2>
  <p>Brimwell brings people together around the events they love. Pick a night out, share it with friends across your social feeds and see the ticket price step down each time someone new commits. Every offer runs for a limited time, so the countdown and participant counter keep everyone in the loop until the doors open.</p>
</section>

<section class="promoted">
  <div class="promo-list">
    <h2>Our Promoted Events</h2>
    <h3>Marisol Vantree parties up Rock</h3>
    <ul>
      <li>Live rock night with guest bands and an open bar hour</li>
      <li>Group tickets drop in price as more friends commit</li>
      <li>Limited time offer with a live countdown on the event page</li>
      <li>Share with your crew and track the participant counter</li>
      <li>Doors open at seven, headline set from nine till late</li>
      <li>Located in the heart of Camden, close to the tube</li>
    </ul>
    <a class="btn-outline" href="#">Get Tickets</a>
  </div>
  <div class="promo-create">
    <div class="create-icon"></div>
    <h2>Create Your Own Event</h2>
    <p>Start a group, invite your friends and unlock a better price together.</p>
    <a class="btn-solid" href="#">Get Started</a>
  </div>
</section>

<section class="categories">
  <h2 class="section-title">Browse by Top Categories</h2>
  <div class="tabs"><a class="is-active" href="#">Today</a><a href="#">This Week</a><a href="#">This Weekend</a><a href="#">This Month</a><a href="#">Anytime</a><a href="#">See All</a></div>
  <div class="tile sports" role="img" aria-label="Motorbike racer leaning into a corner"><h4>Sports &amp; Wellness</h4></div>
  <div class="tile balloons" role="img" aria-label="Colourful hot air balloons rising at sunset"><h4>Balloon Festival</h4></div>
  <div class="tile music" role="img" aria-label="Concert stage with coloured lights"><h4>Music</h4></div>
  <div class="tile festivals" role="img" aria-label="Festival crowd with colour powder in the air"><h4>Festivals</h4></div>
</section>

<footer class="site-footer">
  <div class="foot-col"><h4>Useful Stuff</h4><ul><li>How it Works</li><li>Help Centre</li><li>The Small Print</li></ul></div>
  <div class="foot-col"><h4>Work With Us</h4><ul><li>List My Event</li><li>Affiliate Program</li><li>Partner Enquiries</li></ul></div>
  <div class="foot-col"><h4>Meet Brimwell</h4><ul><li>Our Story</li><li>Press</li><li>Contact Us</li></ul></div>
  <div class="foot-col"><h4>Connect with us</h4><ul><li>Friendloom</li><li>Zephly</li><li>Circlet</li><li>Vidora</li></ul></div>
  <div class="foot-brand"><span></span>BRIMWELL</div>
</footer>
<div class="copyright">Copyright © 2015 · Brimwell Events. All Rights Reserved</div>

</body>
</html>
```